Business card for pediatric occupational therapist

I need a business card design for my independent occupational therapy company. I am a pediatric occupational therapist working with children 0-3 years of age. I would like the card to be clean (not too 'busy') and can include pictures/cartoon-like images of children, or toys such as building blocks, or other images that would be relevant to pediatric therapy. I want it to look professional but also intended to be clear that services provided are for children.
Target Market(s)
Families requiring occupational therapy services for their children (physical, emotional, social needs) - developmental delays
Industry/Entity Type
Rehabilitation
Contact Information for Business Card
Maren Tolsvik OT LLC
Maren Tolsvik, OTR/L
Occupational Therapist
maren.tolsvikOT@brindlemail.com

```html
<!DOCTYPE html>
<html lang="en">
<head>
<meta charset="utf-8">
<title>Maren Tolsvik – Occupational Therapist – Business Cards</title>
<link rel="stylesheet" href="https://fonts.googleapis.com/css2?family=Caveat+Brush&family=Patrick+Hand&family=Ubuntu:wght@500&display=swap">
<style>
  :root {
    --ink-brown: #5a2927;
    --ink-grey: #3b3838;
    --amber: #d3832a;
    --sky: #96aed6;
    --periwinkle: #6473b3;
    --sheet: #fdfbfa;
    --sheet-pattern: #f7eeea;
    --card-white: #ffffff;
    --pattern-cream: #f6e6cf;
    --pattern-amber: #e09a4c;
    --pattern-sky: #adc1e2;
    --skin: #f1cda6;
    --hair-brown: #7a4a3c;
    --hair-ginger: #e8954a;
  }
  * { margin: 0; padding: 0; box-sizing: border-box; }
  html, body { width: 1200px; height: 1200px; overflow: hidden; }
  body { background: var(--sheet); position: relative; font-family: "Ubuntu", sans-serif; }

  .sheet-pattern { position: absolute; inset: 0; background: radial-gradient(circle at 50% 55%, var(--sheet) 0%, var(--sheet-pattern) 100%); }

  .side-tab { position: absolute; top: 107px; width: 69px; height: 247px; background: var(--amber); }
  .side-tab--left { left: 0; border-radius: 0 12px 12px 0; }
  .side-tab--right { right: 0; border-radius: 12px 0 0 12px; }

  .masthead { position: absolute; top: 112px; left: 0; width: 1200px; text-align: center; }
  .masthead__name { font-family: "Caveat Brush", cursive; font-weight: 400; font-size: 148px; line-height: 1; color: var(--ink-brown); letter-spacing: -2px; }
  .masthead__role { font-family: "Patrick Hand", cursive; font-size: 66px; line-height: 1; color: var(--ink-grey); margin-top: -6px; margin-left: 10px; }

  .card { position: absolute; top: 471px; width: 253px; height: 441px; overflow: hidden; box-shadow: 6px 6px 6px rgba(0,0,0,0.35); }
  .card--white { left: 135px; background: var(--card-white); }
  .card--amber { left: 473px; background: var(--amber); }
  .card--sky { left: 799px; background: var(--sky); }

  .card__pattern { position: absolute; inset: 0; }
  .card--white .card__pattern { background: radial-gradient(ellipse at 50% 50%, var(--card-white) 0%, var(--pattern-cream) 130%); }
  .card--amber .card__pattern { background: radial-gradient(ellipse at 50% 50%, var(--amber) 0%, var(--pattern-amber) 130%); }
  .card--sky .card__pattern { background: radial-gradient(ellipse at 50% 50%, var(--sky) 0%, var(--pattern-sky) 130%); }

  .card__brand { position: absolute; left: 0; width: 100%; text-align: center; }
  .card--white .card__brand { top: 144px; color: var(--ink-brown); }
  .card--amber .card__brand, .card--sky .card__brand { top: 118px; color: #ffffff; }
  .card__name { font-family: "Caveat Brush", cursive; font-size: 42px; line-height: 1; letter-spacing: -0.5px; }
  .card__role { font-family: "Patrick Hand", cursive; font-size: 20px; line-height: 1; margin-top: 0; }
  .card--white .card__role { color: #222; }

  .card__portrait { position: absolute; left: 80px; top: 218px; width: 96px; height: 112px; border-radius: 8px; }
  .card--amber .card__portrait { background: linear-gradient(180deg, var(--hair-brown), var(--skin)); }
  .card--sky .card__portrait { top: 218px; height: 128px; background: linear-gradient(180deg, var(--hair-ginger), var(--skin)); }

  .card__contact { position: absolute; left: 15px; top: 342px; color: var(--ink-brown); line-height: 19.6px; }
  .contact__line { display: flex; align-items: center; gap: 6px; white-space: nowrap; font-size: 14.5px; }
  .contact__line--company { padding-left: 20px; font-size: 15px; }
  .contact__line--email { font-size: 13px; }
  .contact__icon { width: 14px; height: 14px; flex: none; }

  .card__tab { position: absolute; left: 58px; bottom: 0; width: 137px; height: 24px; border-radius: 8px 8px 0 0; background: var(--ink-brown); }
  .card--sky .card__tab { background: var(--periwinkle); }
</style>
</head>
<body>
  <div class="sheet-pattern" role="img" aria-label="Faint doodle pattern of toys, hearts and stars"></div>

  <div class="side-tab side-tab--left"></div>
  <div class="side-tab side-tab--right"></div>

  <header class="masthead">
    <h1 class="masthead__name">Maren Tolsvik</h1>
    <p class="masthead__role">Occupational Therapist</p>
  </header>

  <section class="card card--white">
    <div class="card__pattern" role="img" aria-label="Light cream doodle pattern of toys, blocks, bikes and hearts"></div>
    <div class="card__brand">
      <p class="card__name">Maren Tolsvik</p>
      <p class="card__role">Occupational Therapist</p>
    </div>
    <div class="card__contact">
      <p class="contact__line contact__line--company">Maren Tolsvik OT LLC</p>
      <p class="contact__line">
        <svg class="contact__icon" viewBox="0 0 14 14" aria-hidden="true"><rect width="14" height="14" rx="3" fill="#5a2927"/><path d="M4.3 3.2c.4-.3.9-.2 1.1.2l.7 1.3c.2.3.1.7-.2.9l-.5.4c.4.9 1.1 1.6 2 2l.4-.5c.2-.3.6-.4.9-.2l1.3.7c.4.2.5.7.2 1.1l-.6.7c-.4.4-1 .5-1.6.3C6 9.4 4.6 8 3.9 6c-.2-.6-.1-1.2.3-1.6z" fill="#fff"/></svg>
        0000.5550.2718
      </p>
      <p class="contact__line contact__line--email">
        <svg class="contact__icon" viewBox="0 0 14 14" aria-hidden="true"><rect width="14" height="14" rx="3" fill="#5a2927"/><rect x="3" y="4" width="8" height="6" fill="none" stroke="#fff" stroke-width="1"/><path d="M3 4l4 3.2L11 4" fill="none" stroke="#fff" stroke-width="1"/></svg>
        maren.tolsvikOT@brindlemail.com
      </p>
    </div>
    <div class="card__tab"></div>
  </section>

  <section class="card card--amber">
    <div class="card__pattern" role="img" aria-label="Amber doodle pattern of toys, blocks, bikes and hearts"></div>
    <div class="card__brand">
      <p class="card__name">Maren Tolsvik</p>
      <p class="card__role">Occupational Therapist</p>
    </div>
    <div class="card__portrait" role="img" aria-label="Cartoon illustration of a smiling boy"></div>
    <div class="card__tab"></div>
  </section>

  <section class="card card--sky">
    <div class="card__pattern" role="img" aria-label="Blue doodle pattern of toys, blocks, bikes and hearts"></div>
    <div class="card__brand">
      <p class="card__name">Maren Tolsvik</p>
      <p class="card__role">Occupational Therapist</p>
    </div>
    <div class="card__portrait" role="img" aria-label="Cartoon illustration of a smiling girl"></div>
    <div class="card__tab"></div>
  </section>
</body>
</html>
```